Business Card for premium dental clinic

We are a premium dental clinic based in Brasov, Romania with more than 15 year on the market, providing quality dental treatment made by a team of more specialized dentists, working with modern equipment as a solution to beautiful and healthy teeth.

Our current logo for the clinic use 2 square with colors black and gold - dr Corbescu - studio, using family fonts Bodoni, Myriad Pro and Segoe Print.
Depending on the printing we used some gold CMYK background or gold foil picture background or a gold gradient.
We want a business card:
- eye catching business card
- distinguished business card
- premium design
- to keep the color scheme of black and gold
- to attract the customers to spent time reading the information
- modern concept

```html
<!DOCTYPE html>
<html lang="en">
<head>
<meta charset="utf-8">
<title>dr Corbescu studio – business card</title>
<link rel="stylesheet" href="https://fonts.googleapis.com/css2?family=Lato:wght@400;700&family=Oswald:wght@400&display=swap">
<style>
  :root {
    --backdrop: #6e5239;
    --ink-black: #050708;
    --paper-white: #ffffff;
    --gold: #d4892b;
    --gold-light: #f6d45a;
    --gold-mid: #e8b533;
    --gold-deep: #c98f1c;
    --text-dark: #1c1c1c;
  }
  * { box-sizing: border-box; margin: 0; padding: 0; }
  html, body {
    width: 1200px; height: 1023px; overflow: hidden;
    background: var(--backdrop);
  }
  .canvas { position: relative; width: 1200px; height: 1023px; }

  .card {
    position: absolute; left: 248px; width: 681px; height: 390px;
    display: flex; box-shadow: -8px 6px 0 rgba(0,0,0,.55), 0 10px 24px rgba(0,0,0,.35);
  }
  .card--front { top: 87px; }
  .card--back  { top: 541px; }

  .card__half { position: relative; width: 50%; height: 100%; }
  .panel--black { background: var(--ink-black); }
  .panel--white { background: var(--paper-white); }
  .panel--gold {
    background: radial-gradient(circle at 40% 40%, var(--gold-light), var(--gold-mid) 55%, var(--gold-deep));
  }

  .brand-name {
    font-family: "Lato", sans-serif; font-weight: 400;
    color: var(--paper-white); line-height: 1;
  }
  .card--front .brand-name {
    position: absolute; left: 0; right: 0; top: 112px;
    text-align: center; font-size: 44px;
  }
  .brand-name__line { display: block; }
  .brand-name__line + .brand-name__line { margin-top: 22px; font-size: 46px; }

  .contact {
    position: absolute; right: 32px; top: 80px;
    font-family: "Lato", sans-serif; color: var(--text-dark); text-align: right;
  }
  .contact__name { font-size: 35px; font-weight: 700; color: var(--gold); letter-spacing: .5px; line-height: 1; }
  .contact__role { font-size: 17px; margin-top: 8px; }
  .contact__address { font-size: 17px; line-height: 24px; margin-top: 18px; }
  .contact__list { list-style: none; margin-top: 16px; }
  .contact__item {
    display: flex; justify-content: flex-end; align-items: center; gap: 10px;
    font-size: 17px; height: 31px;
  }
  .contact__icon { width: 18px; height: 18px; flex: none; }

  .brand-plate {
    position: absolute; left: 38px; right: 0; top: 124px; height: 142px;
    background: var(--paper-white); display: flex; align-items: center; justify-content: center;
  }
  .brand-plate .brand-name { color: var(--text-dark); font-size: 48px; }

  .panel__studio {
    position: absolute; left: 0; right: 0; top: 165px; text-align: center; font-size: 54px;
  }
  .panel__tagline {
    position: absolute; right: 12px; bottom: 10px;
    font-family: "Oswald", sans-serif; font-weight: 400; font-size: 44px;
    color: var(--paper-white); line-height: 1;
  }
</style>
</head>
<body>
<main class="canvas">

  <section class="card card--front" aria-label="Business card front">
    <div class="card__half panel--black">
      <p class="brand-name">
        <span class="brand-name__line">dr Corbescu</span>
        <span class="brand-name__line">studio</span>
      </p>
    </div>
    <div class="card__half panel--white">
      <div class="contact">
        <h1 class="contact__name">ANDREI POPA</h1>
        <p class="contact__role">Managing Director</p>
        <p class="contact__address">2345 First Address Line<br>Second Address Line, 56324</p>
        <ul class="contact__list">
          <li class="contact__item">123 456 7890
            <svg class="contact__icon" viewBox="0 0 24 24" fill="none" stroke="var(--gold)" stroke-width="2"><path d="M5 3h4l2 5-3 2a12 12 0 0 0 6 6l2-3 5 2v4a2 2 0 0 1-2 2A18 18 0 0 1 3 5a2 2 0 0 1 2-2z"/></svg>
          </li>
          <li class="contact__item">lorem@yourwebsite.com
            <svg class="contact__icon" viewBox="0 0 24 24"><rect x="2" y="5" width="20" height="14" fill="var(--gold)"/><path d="M2 5l10 8 10-8M2 19l8-7M22 19l-8-7" stroke="#fff" stroke-width="1.5" fill="none"/></svg>
          </li>
          <li class="contact__item">www.yourwebsite.com
            <svg class="contact__icon" viewBox="0 0 24 24" fill="none" stroke="var(--gold)" stroke-width="1.6"><circle cx="12" cy="12" r="10"/><ellipse cx="12" cy="12" rx="4.5" ry="10"/><path d="M2 12h20M4 7h16M4 17h16"/></svg>
          </li>
        </ul>
      </div>
    </div>
  </section>

  <section class="card card--back" aria-label="Business card back">
    <div class="card__half panel--gold" role="img" aria-label="Gold foil texture background">
      <div class="brand-plate"><p class="brand-name">dr Corbescu</p></div>
    </div>
    <div class="card__half panel--black">
      <p class="brand-name panel__studio">studio</p>
      <p class="panel__tagline">dental clinic</p>
    </div>
  </section>

</main>
</body>
</html>
```